WordPress WEB DESIGN & CODING for www.quelbrix-aerial.com Wireless Tower Contruction

WEB DESIGN & CODING for www.quelbrix-aerial.com
Wireless Tower Contruction Industry

SLOGAN: SERVICE AT A HIGHER LEVEL

Brannock Spires LLC has been in business since 2014 with combined professional Team experience of over 40 years.

Our Team is composed of long-time industry professionals in every aspect of the wireless telecommunications and commercial construction industries, including project management and site acquisition.

Brannock Spires specializes in providing tower installation services for the Wireless Telecommunications in the Southeastern of the United States.

Our key services are Wireless Tower Construction, Installation & Maintenance

Site audits and Tower mapping
Mount swaps and Modifications
Hardline & Jumper Installation
Antenna & Radio Install, Decom, Testing and Maintenance
Tower Lighting Installation & Testing
Fiber / Sweep / RET/ PIM Testing
Small Cells
Civil installation (concrete/steel platforms/electrical)
____________________________________________________________________

we need a clean yet vibrant, energetic website design that will convey our tower installation work to the fullest... It should use the navy and green colors of our logo and it must be mobile friendly and coded for both Android & IOS;
the site structure:
HOME
ABOUT
SERVICES
CONTRACT
CAREERS
GALLERY

I also attach a few pics we bought on shutterstock so these can be used if needed as we own them...

Target Market(s)

Client: large companies looking for general contractor or installation contractor in the market

Industry/Entity Type

Wireless Communication

Coding

Coded - Design and coding required

Number of Pages Required

4 page

Font styles to use
Sans Serif

Colors
0555a3
00a990
ffffff

Requirements
Must have
• Wordpress - must be both desktop mobile friendly and mobile is the key -
• should open swiftly on both Android & iOS
• See power point file with presentation about the company; page 5 is our keyservices but other contents can be used too
Nice to have
• panorama pics changing from the height/tower view showing the full overview, could be a slideshow or a short video...
Should not have
• flash animation does not work on iOS so this should be avoided.

```html
<!DOCTYPE html>
<html lang="en">
<head>
<meta charset="utf-8">
<title>Brannock Spires — Service at a Higher Level</title>
<link href="https://fonts.googleapis.com/css2?family=Poppins:wght@400;500;600&family=Oswald:wght@300;400&display=swap" rel="stylesheet">
<style>
:root{
  --page:#f3f4f6;
  --navy:#0b4ea2;
  --green:#2f8f2a;
  --green-line:#3a9a2c;
  --ink:#4a4a4a;
  --soft:#f4f6fa;
  --field:#f2f2f2;
  --field-line:#dcdcdc;
  --dark:#231f20;
  --white:#ffffff;
}
*{box-sizing:border-box;margin:0;padding:0}
html,body{width:722px;height:1200px;overflow:hidden;background:var(--page)}
body{font-family:'Poppins',sans-serif;color:var(--ink)}
.stage{position:absolute;left:0;top:0;width:1484px;height:2467px;transform:scale(.48652);transform-origin:0 0}
.screen{position:absolute;background:var(--white);overflow:hidden}
.screen.mobile{left:208px;top:208px;width:249px;height:2050px}
.screen.desktop{left:564px;top:208px;width:712px;height:2051px}
.abs{position:absolute}
.center{text-align:center;left:0;right:0}
.photo{position:absolute}
.photo.hero{background:
  radial-gradient(ellipse 38% 30% at 58% 92%,rgba(255,255,255,.95) 0%,rgba(240,245,252,.6) 45%,rgba(255,255,255,0) 100%),
  radial-gradient(ellipse 30% 40% at 88% 72%,rgba(238,242,248,.95) 0%,rgba(220,228,240,.5) 55%,rgba(255,255,255,0) 100%),
  radial-gradient(ellipse 25% 20% at 15% 92%,rgba(230,236,245,.8) 0%,rgba(255,255,255,0) 100%),
  radial-gradient(ellipse 60% 80% at 55% 100%,rgba(200,215,235,.55) 0%,rgba(255,255,255,0) 70%),
  linear-gradient(172deg,#2f4f82 0%,#486da3 35%,#6e8fbd 70%,#9db3d2 100%)}
.photo.sunset{background:
  radial-gradient(circle at 52% 42%,#fff6da 0%,#f3d08f 14%,rgba(214,170,100,.6) 35%,rgba(0,0,0,0) 60%),
  linear-gradient(180deg,#c99d5c 0%,#a67c45 50%,#4a3826 85%,#2c221a 100%)}
.photo.sunburst{background:
  radial-gradient(circle at 40% 72%,#ffffff 0%,#f1f5fb 10%,rgba(215,228,244,.7) 28%,rgba(255,255,255,0) 55%),
  radial-gradient(ellipse 40% 35% at 78% 45%,rgba(235,240,248,.9) 0%,rgba(255,255,255,0) 100%),
  linear-gradient(160deg,#2a4f8c 0%,#4f77b1 45%,#9fb6d6 100%)}
.photo.grey{background:
  radial-gradient(ellipse 70% 50% at 50% 20%,#f7f7f8 0%,rgba(247,247,248,0) 100%),
  linear-gradient(180deg,#ececed 0%,#d4d4d6 70%,#a9a9ac 100%)}
.photo.steel{background:
  radial-gradient(circle at 50% 50%,#f2f2f3 0%,#cfcfd2 30%,#8e8e93 70%,#5c5c61 100%)}
.photo.bluesky{background:
  radial-gradient(ellipse 30% 20% at 80% 18%,rgba(255,255,255,.8) 0%,rgba(255,255,255,0) 100%),
  radial-gradient(ellipse 45% 25% at 30% 85%,rgba(240,245,252,.8) 0%,rgba(255,255,255,0) 100%),
  linear-gradient(180deg,#3d6fb4 0%,#6b93c8 55%,#a9c0de 100%)}
.photo.cloud{background:
  radial-gradient(ellipse 45% 22% at 75% 30%,rgba(255,255,255,.9) 0%,rgba(255,255,255,0) 100%),
  radial-gradient(ellipse 55% 25% at 25% 65%,rgba(250,252,255,.85) 0%,rgba(255,255,255,0) 100%),
  radial-gradient(ellipse 50% 18% at 70% 92%,rgba(245,248,252,.9) 0%,rgba(255,255,255,0) 100%),
  linear-gradient(180deg,#5f88c0 0%,#7fa0cd 50%,#a8bfdc 100%)}
.photo.video{background:
  radial-gradient(ellipse 25% 18% at 20% 20%,rgba(255,255,255,.8) 0%,rgba(255,255,255,0) 100%),
  radial-gradient(ellipse 30% 15% at 85% 15%,rgba(255,255,255,.85) 0%,rgba(255,255,255,0) 100%),
  radial-gradient(ellipse 70% 22% at 50% 92%,rgba(245,248,252,.9) 0%,rgba(255,255,255,0) 100%),
  linear-gradient(180deg,#6a93c9 0%,#88a9d4 55%,#b2c7e1 100%)}
.logo-name{position:absolute;font-weight:600;color:var(--navy);white-space:nowrap;letter-spacing:.2px}
.footer .logo-name{color:var(--white)}
.call-label{position:absolute;color:var(--navy);font-weight:500;line-height:1}
.call-num{position:absolute;font-family:'Oswald',sans-serif;font-weight:300;color:var(--navy);line-height:1}
.hero-title{position:absolute;color:var(--white);font-weight:600;letter-spacing:.5px;text-shadow:0 1px 3px rgba(0,0,0,.25)}
.btn{position:absolute;display:flex;align-items:center;justify-content:center;gap:5px;color:var(--white);font-weight:500;text-transform:uppercase;letter-spacing:.3px;white-space:nowrap}
.btn.green{background:var(--green)}
.btn.navy{background:var(--navy)}
.btn.outline{border:1px solid rgba(255,255,255,.8)}
.btn svg{flex:none}
.heading{position:absolute;color:var(--navy);font-weight:600;letter-spacing:.4px}
.copy{position:absolute;text-align:center;line-height:1.6}
.service{position:absolute;background:var(--navy);color:var(--white)}
.service h3{position:absolute;font-weight:500;line-height:1.15}
.service p{position:absolute;line-height:1.6}
.service ul{position:absolute;list-style:none;line-height:1.75}
.service li{display:flex;align-items:center;gap:4px}
.pointer{position:absolute;width:0;height:0;border-top:6px solid transparent;border-bottom:6px solid transparent}
.section-soft{position:absolute;background:var(--soft)}
.video-card{position:absolute;background:var(--white)}
.video-title{position:absolute;color:var(--white);font-weight:500;letter-spacing:.5px;text-align:center}
.field{position:absolute;background:var(--field);border:1px solid var(--field-line);color:#8a8a8a;padding-left:7px;display:flex;align-items:center}
.field.area{align-items:flex-start;padding-top:5px}
.field .chev{position:absolute;right:8px}
.footer{position:absolute;left:0;right:0;background:var(--dark);color:#e5e5e5}
.foot-head{position:absolute;color:var(--white);font-weight:500}
.foot-text{position:absolute;color:#d0d0d0;line-height:1.5}
.foot-links{position:absolute;list-style:none;color:#cfcfcf}
.rule{position:absolute;height:1px;background:#4a4547}
.social{position:absolute;border:1px solid var(--green-line);border-radius:50%}
.social.on{background:var(--green-line)}
.accent{color:var(--green-line)}
.nav{position:absolute;color:var(--navy);font-weight:500;font-size:5.5px;letter-spacing:.2px}
.hamburger{position:absolute;border:1px solid var(--green);border-radius:2px}
.hamburger span{position:absolute;left:4px;right:4px;height:1px;background:var(--green)}
</style>
</head>
<body>
<div class="stage">

  <!-- ============ MOBILE ============ -->
  <section class="screen mobile">
    <header>
      <div class="logo-name" style="left:12px;top:18px;font-size:9.5px">Brannock Spires</div>
      <svg class="abs" style="left:104px;top:18px" width="15" height="15" viewBox="0 0 16 16"><circle cx="8" cy="8" r="7" fill="none" stroke="#2f8f2a" stroke-width="1.3"/><path d="M5.3 4.6l1.4-.4.9 1.9-.9.7c.4 1 1.3 1.9 2.3 2.3l.7-.9 1.9.9-.4 1.4c-3.2.2-6.1-2.7-5.9-5.9z" fill="#2f8f2a"/></svg>
      <div class="call-label" style="left:125px;top:15px;font-size:7px">Call Us:</div>
      <div class="call-num" style="left:125px;top:24px;font-size:10px">123-555-0187</div>
      <div class="hamburger" style="left:218px;top:15px;width:18px;height:18px"><span style="top:5px"></span><span style="top:8px"></span><span style="top:11px"></span></div>
    </header>

    <div class="photo hero" style="left:0;top:47px;width:249px;height:150px" role="img" aria-label="Lattice communications tower against a blue sky with sun rays and sunlit clouds"></div>
    <div class="hero-title center" style="top:99px;font-size:13px;text-align:center">SERVICE AT A HIGHER LEVEL</div>
    <div class="btn green" style="left:68px;top:127px;width:112px;height:18px;font-size:6.5px">Reaquest a quote</div>
    <svg class="abs" style="left:0;top:165px" width="249" height="36" viewBox="0 0 249 36"><path d="M0 30 Q124.5 -8 249 30 L249 36 L0 36Z" fill="#fff"/><path d="M40 17 Q124.5 2 209 17" fill="none" stroke="#3a9a2c" stroke-width="2"/></svg>

    <h2 class="heading center" style="top:218px;font-size:12px;text-align:center">DISCOVER ABOUT US</h2>
    <p class="copy" style="left:17px;width:215px;top:245px;font-size:8px">Brannock Spires LLC has been in business since 2014 with combined professional Team experience of over 40 years.</p>
    <p class="copy" style="left:14px;width:221px;top:290px;font-size:8px">Our Team is composed of long-time industry professionals in every aspect of the wireless tele-communications and commercial construction industries, including project ...</p>
    <div class="btn green" style="left:83px;top:357px;width:83px;height:18px;font-size:6.5px">Read more <svg width="7" height="7" viewBox="0 0 8 8"><circle cx="4" cy="4" r="3.3" fill="none" stroke="#fff"/><path d="M3.3 2.4L5 4 3.3 5.6" fill="none" stroke="#fff"/></svg></div>

    <h2 class="heading center" style="top:420px;font-size:12px;text-align:center">OUR SERVICES</h2>

    <div class="photo grey" style="left:0;top:451px;width:89px;height:141px" role="img" aria-label="Several lattice towers with antennas viewed from below"></div>
    <div class="service" style="left:89px;top:451px;width:160px;height:141px">
      <div class="pointer" style="left:-1px;top:64px;border-left:6px solid #e2e2e3"></div>
      <h3 style="left:18px;top:13px;font-size:10px">Wireless Tower<br>Construction</h3>
      <p style="left:18px;top:46px;width:130px;font-size:8px">Brannock Spires LLC has been in business since 2014 with combined professional Team experience of over 40 years.</p>
      <div class="btn outline" style="left:18px;top:110px;width:83px;height:19px;font-size:6.5px">Read more <svg width="7" height="7" viewBox="0 0 8 8"><circle cx="4" cy="4" r="3.3" fill="none" stroke="#fff"/><path d="M3.3 2.4L5 4 3.3 5.6" fill="none" stroke="#fff"/></svg></div>
    </div>

    <div class="service" style="left:0;top:597px;width:160px;height:141px">
      <h3 style="left:12px;top:13px;font-size:10px">Installation<br>&amp; Maintenance</h3>
      <p style="left:12px;top:46px;width:140px;font-size:8px;text-align:left">Our Integrators and BTS Technicians are Trained, Experienced and Certified in Commissioning ...</p>
      <div class="btn outline" style="left:12px;top:110px;width:83px;height:19px;font-size:6.5px">Read more <svg width="7" height="7" viewBox="0 0 8 8"><circle cx="4" cy="4" r="3.3" fill="none" stroke="#fff"/><path d="M3.3 2.4L5 4 3.3 5.6" fill="none" stroke="#fff"/></svg></div>
    </div>
    <div class="photo cloud" style="left:160px;top:597px;width:89px;height:141px" role="img" aria-label="Tower platform with antenna mounts against cloudy sky"></div>

    <div class="section-soft" style="left:0;top:738px;width:249px;height:434px"></div>
    <h2 class="heading center" style="top:782px;font-size:12px;text-align:center">OUR WORK</h2>
    <div class="photo sunset" style="left:11px;top:813px;width:110px;height:109px" role="img" aria-label="Tower seen from below against a golden sky with the sun behind it"></div>
    <div class="photo steel" style="left:127px;top:813px;width:110px;height:109px" role="img" aria-label="Looking up through the inside of a steel lattice tower"></div>
    <div class="photo grey" style="left:11px;top:928px;width:110px;height:109px" role="img" aria-label="Antenna-laden towers in black and white"></div>
    <div class="photo sunburst" style="left:127px;top:928px;width:110px;height:109px" role="img" aria-label="Tower with sunburst through clouds"></div>
    <div class="btn navy" style="left:83px;top:1056px;width:83px;height:19px;font-size:6.5px">View all <svg width="7" height="7" viewBox="0 0 8 8"><circle cx="4" cy="4" r="3.3" fill="none" stroke="#fff"/><path d="M3.3 2.4L5 4 3.3 5.6" fill="none" stroke="#fff"/></svg></div>

    <div class="video-card" style="left:11px;top:1105px;width:226px;height:127px"></div>
    <div class="photo video" style="left:24px;top:1117px;width:202px;height:107px" role="img" aria-label="Two communication towers against a blue sky, video preview"></div>
    <svg class="abs" style="left:117px;top:1155px" width="16" height="16" viewBox="0 0 16 16"><circle cx="8" cy="8" r="7" fill="none" stroke="#fff" stroke-width="1.2"/><path d="M6.3 5v6l4.7-3z" fill="none" stroke="#fff" stroke-width="1.1"/></svg>
    <div class="video-title center" style="top:1175px;font-size:11px">FULL OVERVIEW</div>

    <h2 class="heading center" style="top:1275px;font-size:12px;text-align:center">CONTACT BRANNOCK SPIRES</h2>
    <p class="copy" style="left:17px;width:215px;top:1296px;font-size:8px">Contact us today for a free consultation <span class="accent" style="font-family:'Oswald',sans-serif">123-555-0187</span> or complete the below form. We will respond to your enquiry as soon as possible.</p>
    <div class="field" style="left:24px;top:1361px;width:201px;height:18px;font-size:7px">Name</div>
    <div class="field" style="left:24px;top:1388px;width:201px;height:18px;font-size:7px">Email</div>
    <div class="field" style="left:24px;top:1414px;width:201px;height:18px;font-size:7px">Phone</div>
    <div class="field" style="left:24px;top:1440px;width:201px;height:18px;font-size:7px">Select your services<svg class="chev" width="6" height="4" viewBox="0 0 6 4"><path d="M.5.5L3 3 5.5.5" fill="none" stroke="#888"/></svg></div>
    <div class="field area" style="left:24px;top:1467px;width:201px;height:45px;font-size:7px">Message ..</div>
    <div class="btn navy" style="left:83px;top:1522px;width:83px;height:19px;font-size:6.5px">Submit <svg width="7" height="6" viewBox="0 0 7 6"><path d="M0 0L7 3 0 6 1.5 3z" fill="#fff"/></svg></div>

    <svg class="abs" style="left:0;top:1550px" width="249" height="40" viewBox="0 0 249 40"><path d="M0 3 Q124.5 50 249 3 L249 40 L0 40Z" fill="#231f20"/><path d="M0 12 Q124.5 50 249 12" fill="none" stroke="#3a9a2c" stroke-width="2"/></svg>
    <footer class="footer" style="top:1589px;height:461px">
      <div class="logo-name center" style="top:18px;font-size:12px;text-align:center">Brannock Spires</div>
      <div class="rule" style="left:11px;width:226px;top:65px"></div>
      <div class="foot-head" style="left:23px;top:80px;font-size:10px">Contact Us</div>
      <div class="foot-text" style="left:23px;top:106px;font-size:9px"><span class="accent" style="font-family:'Oswald',sans-serif;font-weight:300">Call Us: ✆</span> <span style="font-family:'Oswald',sans-serif;font-weight:300;color:#fff">+123-555-0187</span></div>
      <div class="foot-text" style="left:23px;top:123px;font-size:8px"><span class="accent">e.</span> info@brannockspires.com</div>
      <div class="foot-text" style="left:23px;top:150px;font-size:8px;width:190px">4410 Ridgeway Industrial Pkwy Dalton,<br>GA 30721</div>
      <div class="rule" style="left:11px;width:226px;top:191px"></div>
      <div class="foot-head" style="left:23px;top:207px;font-size:10px">Quick Links</div>
      <ul class="foot-links" style="left:23px;top:229px;font-size:8px;line-height:14.4px"><li>Home</li><li>About</li><li>Services</li><li>Contract</li><li>Careers</li><li>Gallery</li><li>Contact Us</li></ul>
      <ul class="foot-links" style="left:87px;top:229px;font-size:8px;line-height:14.4px"><li>Tearms &amp; Conditions</li><li>Privacy Policy</li><li>Site Map</li><li>Disclaimer</li></ul>
      <div class="rule" style="left:11px;width:226px;top:343px"></div>
      <div class="foot-head" style="left:23px;top:357px;font-size:10px">Follow Us</div>
      <div class="social" style="left:23px;top:383px;width:18px;height:18px"></div>
      <div class="social on" style="left:49px;top:383px;width:18px;height:18px"></div>
      <div class="social" style="left:75px;top:383px;width:18px;height:18px"></div>
      <div class="social" style="left:101px;top:383px;width:18px;height:18px"></div>
      <svg class="abs" style="left:212px;top:375px" width="12" height="12" viewBox="0 0 12 12"><path d="M1 11L6 1l5 10M3.5 7h5" fill="none" stroke="#3a9a2c" stroke-width="1.3"/></svg>
      <div class="rule" style="left:11px;width:226px;top:421px"></div>
      <div class="foot-text center" style="top:436px;font-size:8px;text-align:center">© 2019 <span class="accent">Brannock Spires</span>. All Rights Reseved</div>
    </footer>
  </section>

  <!-- ============ DESKTOP ============ -->
  <section class="screen desktop">
    <header>
      <div class="logo-name" style="left:86px;top:19px;font-size:11px">Brannock Spires</div>
      <nav>
        <span class="nav" style="left:237px;top:22px">HOME</span>
        <span class="nav" style="left:272px;top:22px">ABOUT</span>
        <span class="nav" style="left:309px;top:22px">SERVICES</span>
        <span class="nav" style="left:355px;top:22px">CONTRACT</span>
        <span class="nav" style="left:406px;top:22px">CAREERS</span>
        <span class="nav" style="left:451px;top:22px">GALLERY</span>
        <span class="nav" style="left:493px;top:22px">CONTACT US</span>
        <div class="abs" style="left:231px;top:47px;width:31px;height:2px;background:var(--green)"></div>
      </nav>
      <svg class="abs" style="left:554px;top:17px" width="16" height="16" viewBox="0 0 16 16"><circle cx="8" cy="8" r="7" fill="none" stroke="#2f8f2a" stroke-width="1.3"/><path d="M5.3 4.6l1.4-.4.9 1.9-.9.7c.4 1 1.3 1.9 2.3 2.3l.7-.9 1.9.9-.4 1.4c-3.2.2-6.1-2.7-5.9-5.9z" fill="#2f8f2a"/></svg>
      <div class="call-label" style="left:577px;top:15px;font-size:7px">Call Us:</div>
      <div class="call-num" style="left:577px;top:25px;font-size:10px">123-555-0187</div>
    </header>

    <div class="photo hero" style="left:0;top:50px;width:712px;height:340px" role="img" aria-label="Lattice communications tower rising into blue sky with sun rays and clouds"></div>
    <div class="hero-title center" style="top:178px;font-size:20px;text-align:center">SERVICE AT A HIGHER LEVEL</div>
    <div class="btn green" style="left:308px;top:216px;width:96px;height:20px;font-size:6px">Reaquest a quote</div>
    <svg class="abs" style="left:0;top:322px" width="712" height="72" viewBox="0 0 712 72"><path d="M0 68 Q356 -50 712 68 L712 72 L0 72Z" fill="#fff"/><path d="M50 60 Q356 -38 662 60" fill="none" stroke="#3a9a2c" stroke-width="3"/></svg>

    <h2 class="heading center" style="top:408px;font-size:14px;text-align:center">DISCOVER ABOUT US</h2>
    <p class="copy" style="left:146px;width:420px;top:442px;font-size:5.8px">Brannock Spires LLC has been in business since 2014 with combined professional Team experience of over 40 years.</p>
    <p class="copy" style="left:146px;width:420px;top:460px;font-size:5.8px">Our Team is composed of long-time industry professionals in every aspect of the wireless telecommunications and commercial construction industries, including project management and site acquisition.</p>
    <p class="copy" style="left:146px;width:420px;top:488px;font-size:5.8px">Brannock Spires specializes in providing turn-key service by integrating services for the Wireless Telecommunications and Commercial Construction industries, maintaining a footprint throughout the South Eastern, Central and Midwest regions of the United States.</p>
    <div class="btn green" style="left:318px;top:536px;width:76px;height:20px;font-size:5.5px">Read more <svg width="6" height="6" viewBox="0 0 8 8"><circle cx="4" cy="4" r="3.3" fill="none" stroke="#fff"/><path d="M3.3 2.4L5 4 3.3 5.6" fill="none" stroke="#fff"/></svg></div>

    <h2 class="heading center" style="top:626px;font-size:14px;text-align:center">OUR SERVICES</h2>

    <div class="photo grey" style="left:0;top:663px;width:152px;height:211px" role="img" aria-label="Tall lattice towers with antennas in grey sky"></div>
    <div class="service" style="left:152px;top:663px;width:204px;height:211px">
      <div class="pointer" style="left:-1px;top:98px;border-left:6px solid #dadadc"></div>
      <h3 style="left:21px;top:26px;font-size:9px">Wireless Tower Construction</h3>
      <p style="left:21px;top:50px;width:165px;font-size:5.3px">Brannock Spires LLC has been in business since 2014 with combined professional Team experience of over 40 years.</p>
      <ul style="left:21px;top:86px;width:170px;font-size:5.3px">
        <li><svg width="6" height="5" viewBox="0 0 6 5"><path d="M.5 2.5l1.7 1.7L5.5.6" fill="none" stroke="#fff"/></svg>Site audits and Tower mapping</li>
        <li><svg width="6" height="5" viewBox="0 0 6 5"><path d="M.5 2.5l1.7 1.7L5.5.6" fill="none" stroke="#fff"/></svg>Mount swaps and Modifications</li>
        <li><svg width="6" height="5" viewBox="0 0 6 5"><path d="M.5 2.5l1.7 1.7L5.5.6" fill="none" stroke="#fff"/></svg>Hardline &amp; Jumper Installation</li>
        <li style="align-items:flex-start"><svg width="6" height="5" viewBox="0 0 6 5" style="margin-top:3px"><path d="M.5 2.5l1.7 1.7L5.5.6" fill="none" stroke="#fff"/></svg><span style="line-height:1.6">Antenna &amp; Radio Install, Decom, Testing and Maintenance</span></li>
        <li><svg width="6" height="5" viewBox="0 0 6 5"><path d="M.5 2.5l1.7 1.7L5.5.6" fill="none" stroke="#fff"/></svg>Tower Lighting Installation &amp; Testing</li>
      </ul>
      <div class="btn outline" style="left:21px;top:163px;width:76px;height:20px;font-size:5.5px">Read more <svg width="6" height="6" viewBox="0 0 8 8"><circle cx="4" cy="4" r="3.3" fill="none" stroke="#fff"/><path d="M3.3 2.4L5 4 3.3 5.6" fill="none" stroke="#fff"/></svg></div>
    </div>
    <div class="photo cloud" style="left:356px;top:663px;width:153px;height:211px" role="img" aria-label="Tower platform with antenna mounts under cloudy sky"></div>
    <div class="service" style="left:509px;top:663px;width:203px;height:211px">
      <div class="pointer" style="left:-1px;top:98px;border-left:6px solid #8eaad2"></div>
      <h3 style="left:21px;top:26px;font-size:9px">Installation &amp; Maintenance</h3>
      <p style="left:21px;top:50px;width:170px;font-size:5.3px">Our Integrators and BTS Technicians are Trained, Experienced and Certified in Commissioning, Integration and Maintenance of Wireless Telecommunications Systems.</p>
      <ul style="left:21px;top:96px;width:170px;font-size:5.3px">
        <li><svg width="6" height="5" viewBox="0 0 6 5"><path d="M.5 2.5l1.7 1.7L5.5.6" fill="none" stroke="#fff"/></svg>Integration</li>
        <li><svg width="6" height="5" viewBox="0 0 6 5"><path d="M.5 2.5l1.7 1.7L5.5.6" fill="none" stroke="#fff"/></svg>Commissioning</li>
        <li><svg width="6" height="5" viewBox="0 0 6 5"><path d="M.5 2.5l1.7 1.7L5.5.6" fill="none" stroke="#fff"/></svg>Call Testing</li>
        <li><svg width="6" height="5" viewBox="0 0 6 5"><path d="M.5 2.5l1.7 1.7L5.5.6" fill="none" stroke="#fff"/></svg>Software Upgrades</li>
        <li><svg width="6" height="5" viewBox="0 0 6 5"><path d="M.5 2.5l1.7 1.7L5.5.6" fill="none" stroke="#fff"/></svg>Card Installation / Decom / Harvesting</li>
      </ul>
      <div class="btn outline" style="left:21px;top:163px;width:76px;height:20px;font-size:5.5px">Read more <svg width="6" height="6" viewBox="0 0 8 8"><circle cx="4" cy="4" r="3.3" fill="none" stroke="#fff"/><path d="M3.3 2.4L5 4 3.3 5.6" fill="none" stroke="#fff"/></svg></div>
    </div>

    <div class="section-soft" style="left:0;top:874px;width:712px;height:578px"></div>
    <h2 class="heading center" style="top:944px;font-size:14px;text-align:center">OUR WORK</h2>
    <div class="photo sunset" style="left:85px;top:980px;width:152px;height:148px" role="img" aria-label="Tower seen from below against a golden sky with the sun behind it"></div>
    <div class="photo sunburst" style="left:242px;top:980px;width:228px;height:148px" role="img" aria-label="Tower with sunburst through clouds"></div>
    <div class="photo grey" style="left:475px;top:980px;width:152px;height:148px" role="img" aria-label="Distant antenna towers in pale sky"></div>
    <div class="photo bluesky" style="left:85px;top:1133px;width:190px;height:148px" role="img" aria-label="Antenna-laden towers against deep blue sky"></div>
    <div class="photo steel" style="left:280px;top:1133px;width:152px;height:148px" role="img" aria-label="Looking up through the inside of a steel lattice tower"></div>
    <div class="photo grey" style="left:437px;top:1133px;width:190px;height:148px" role="img" aria-label="Cluster of telecom towers in black and white"></div>
    <div class="btn navy" style="left:318px;top:1303px;width:76px;height:20px;font-size:5.5px">View all <svg width="6" height="6" viewBox="0 0 8 8"><circle cx="4" cy="4" r="3.3" fill="none" stroke="#fff"/><path d="M3.3 2.4L5 4 3.3 5.6" fill="none" stroke="#fff"/></svg></div>

    <div class="video-card" style="left:131px;top:1367px;width:450px;height:220px"></div>
    <div class="photo video" style="left:148px;top:1383px;width:416px;height:169px" role="img" aria-label="Two communication towers against a blue sky, video preview"></div>
    <svg class="abs" style="left:345px;top:1445px" width="22" height="22" viewBox="0 0 16 16"><circle cx="8" cy="8" r="7" fill="none" stroke="#fff" stroke-width="1"/><path d="M6.3 5v6l4.7-3z" fill="none" stroke="#fff" stroke-width="1"/></svg>
    <div class="video-title center" style="top:1474px;font-size:14px">FULL OVERVIEW</div>

    <h2 class="heading center" style="top:1622px;font-size:14px;text-align:center">CONTACT BRANNOCK SPIRES</h2>
    <p class="copy" style="left:146px;width:420px;top:1651px;font-size:5.8px">Contact us today for a free consultation <span class="accent" style="font-family:'Oswald',sans-serif">123-555-0187</span> or complete the below form.<br>We will respond to your enquiry as soon as possible.</p>
    <div class="field" style="left:148px;top:1691px;width:203px;height:16px;font-size:5.5px">Name</div>
    <div class="field" style="left:360px;top:1691px;width:204px;height:16px;font-size:5.5px">Email</div>
    <div class="field" style="left:148px;top:1717px;width:203px;height:16px;font-size:5.5px">Phone</div>
    <div class="field" style="left:360px;top:1717px;width:204px;height:16px;font-size:5.5px">Select your services<svg class="chev" width="6" height="4" viewBox="0 0 6 4"><path d="M.5.5L3 3 5.5.5" fill="none" stroke="#888"/></svg></div>
    <div class="field area" style="left:148px;top:1742px;width:416px;height:41px;font-size:5.5px">Message ..</div>
    <div class="btn navy" style="left:318px;top:1793px;width:76px;height:20px;font-size:5.5px">Submit <svg width="6" height="5" viewBox="0 0 7 6"><path d="M0 0L7 3 0 6 1.5 3z" fill="#fff"/></svg></div>

    <svg class="abs" style="left:0;top:1800px" width="712" height="80" viewBox="0 0 712 80"><path d="M0 0 Q356 112 712 0 L712 80 L0 80Z" fill="#231f20"/><path d="M40 18 Q356 106 672 18" fill="none" stroke="#3a9a2c" stroke-width="3"/></svg>
    <footer class="footer" style="top:1879px;height:172px">
      <div class="logo-name" style="left:86px;top:40px;font-size:12px">Brannock Spires</div>
      <div class="foot-head" style="left:224px;top:25px;font-size:8px">Contact Us</div>
      <div class="foot-text" style="left:224px;top:46px;font-size:7px"><span class="accent" style="font-family:'Oswald',sans-serif;font-weight:300">Call Us: ✆</span> <span style="font-family:'Oswald',sans-serif;font-weight:300;color:#fff">+123-555-0187</span></div>
      <div class="foot-text" style="left:224px;top:60px;font-size:5.5px"><span class="accent">e.</span> info@brannockspires.com</div>
      <div class="foot-text" style="left:224px;top:82px;font-size:5.5px">4410 Ridgeway Industrial Pkwy<br>Dalton, GA 30721</div>
      <div class="foot-head" style="left:364px;top:25px;font-size:8px">Quick Links</div>
      <ul class="foot-links" style="left:364px;top:46px;font-size:5.5px;line-height:10.2px"><li>Home</li><li>About</li><li>Services</li><li>Contract</li><li>Careers</li><li>Gallery</li><li>Contact Us</li></ul>
      <ul class="foot-links" style="left:410px;top:46px;font-size:5.5px;line-height:10.2px"><li>Tearms &amp; Conditions</li><li>Privacy Policy</li><li>Site Map</li><li>Disclaimer</li></ul>
      <div class="foot-head" style="left:504px;top:25px;font-size:8px">Follow Us</div>
      <div class="social" style="left:504px;top:49px;width:14px;height:14px"></div>
      <div class="social on" style="left:525px;top:49px;width:14px;height:14px"></div>
      <div class="social" style="left:546px;top:49px;width:14px;height:14px"></div>
      <div class="social" style="left:567px;top:49px;width:14px;height:14px"></div>
      <div class="rule" style="left:85px;width:547px;top:135px"></div>
      <div class="foot-text center" style="top:146px;font-size:5.5px;text-align:center">© 2019 <span class="accent">Brannock Spires</span>. All Rights Reseved</div>
      <svg class="abs" style="left:622px;top:144px" width="10" height="10" viewBox="0 0 12 12"><path d="M1 11L6 1l5 10M3.5 7h5" fill="none" stroke="#3a9a2c" stroke-width="1.3"/></svg>
    </footer>
  </section>

</div>
</body>
</html>
```